Enrollment Campaign

We need a flyer design for our school's enrollment campaign. Our school website is www.tbacademy.net.

The flyer should be double sided.

I want the reader to get the following messages:
1. Montessori graduates are leading the top companies of our time.
2. We are an accredited Montessori school.
3. Enrollment is open now for all four programs:
a) Toddler: 18months (or as soon as the child is able to walk) - 3 years
b) CASA: Preschool to Senior Kindergarten (3 years to 6 years)
c) Elementary: Grades 1 to 6
d) Junior High: Grades 7 to 8
4) Our contact information:
website, email:info@tbacademy.net, phone: 416 527 3962
5) Call for Action: Book a Tour! (there is a button on our website to book a tour)
6) In the languages punjabi, hindi and italian, I wouldn't readers to know that we offer their faith and cultural education as well.
7) Fees for children under age of 6 can be claimed in Taxes as day care expense. So, there is no reason to miss providing our children the best that we can in education.
Updates

Please note my updates to my brief in the "must have" section. Also, I have added some pics that can be used. Please note that I don't have one pic (the farming one referred to in my brief). I will really appreciate if you can kindly update your design accordingly.

Project Deadline Extended
Reason: Because of my recent update to the brief, some designers need some time to adjust their designs. I really appreciate your patience and kind consideration for my project. Thank you!

Industry/Entity Type

Education

Colors

Designer to choose colors to be used in the design.

Requirements
Must have
• Must have a unique design. I don't want a typical flyer. The design should be unique and memorable.

One of the main pics that I need is for illustrating a key feature of our new Junior High program that we are starting in August 2015. The key feature is that children are going to be operating a 'greenhouse', growing organic produce and will also be preparing their daily lunch from scratch. So, show a pic of a 13-14year old farming or something.

```html
<!DOCTYPE html>
<html lang="en">
<head>
<meta charset="utf-8">
<title>TB Academy – Enrollment Flyer</title>
<link href="https://fonts.googleapis.com/css2?family=Lora:wght@400;700&family=Lato:wght@400;700&family=Teko:wght@400;500&display=swap" rel="stylesheet">
<style>
:root{
  --blue:#1d9bd7;
  --blue-deep:#0e77b8;
  --blue-light:#49b6e6;
  --green:#b5d334;
  --green-dark:#5d8a12;
  --ink:#333333;
  --white:#ffffff;
  --pin:#e0262b;
  --arrow:#0d5e93;
}
*{margin:0;padding:0;box-sizing:border-box}
html,body{width:991px;height:1200px;overflow:hidden;background:#f2f2f2}
.flyer{position:relative;width:991px;height:1200px;overflow:hidden;font-family:"Lato",sans-serif;color:var(--white)}
.backdrop{position:absolute;inset:0}
.brand{position:absolute;left:33px;top:34px;font-family:"Lora",serif;font-size:58px;font-weight:400;color:var(--blue)}
.headline{position:absolute;left:33px;top:118px;font-family:"Lora",serif;font-size:33px;line-height:42px;color:var(--ink)}
.photo{position:absolute;overflow:hidden}
.photo-stage{left:224px;top:240px;width:230px;height:130px;border:6px solid var(--green);transform:rotate(-6deg);
  background:linear-gradient(135deg,#f3f0ea 0%,#d8c6b4 45%,#c9473a 60%,#efe9e1 100%);box-shadow:0 3px 8px rgba(0,0,0,.3)}
.pin{position:absolute;left:445px;top:226px;width:18px;height:18px;border-radius:50%;background:var(--pin);box-shadow:0 2px 3px rgba(0,0,0,.35)}
.enroll-title{position:absolute;left:33px;top:408px;font-family:"Lora",serif;font-weight:700;font-size:27px;line-height:32px;color:var(--green)}
.programs{position:absolute;left:33px;top:486px;list-style:none;font-family:"Lora",serif;font-size:16px;line-height:22px}
.programs li::before{content:"➤";color:var(--green);margin-right:8px}
.programs b{text-transform:uppercase}
.badge{position:absolute;left:686px;top:393px;width:280px;height:280px}
.badge-text{position:absolute;left:686px;top:452px;width:280px;text-align:center;font-family:"Lato",sans-serif;line-height:34px}
.badge-text .lead{display:block;font-size:29px;color:var(--green-dark)}
.badge-text .strong{display:block;font-size:29px;font-weight:700;color:var(--white);text-shadow:0 0 3px var(--green-dark),0 0 3px var(--green-dark)}
.languages{position:absolute;left:33px;top:598px;font-family:"Teko",sans-serif;font-size:48px;line-height:48px;font-weight:500;letter-spacing:.5px}
.languages .accent{color:var(--green)}
.faith{position:absolute;left:33px;top:650px;font-family:"Teko",sans-serif;font-size:29px;line-height:30px;letter-spacing:.5px}
.moment{position:absolute;width:236px;height:236px;border-radius:50%;border:10px solid var(--green);top:700px}
.moment-one{left:63px;background:radial-gradient(circle at 45% 40%,#f1ece6 0%,#d2b08a 55%,#b58457 100%)}
.moment-two{left:387px;background:radial-gradient(circle at 50% 35%,#f4eadb 0%,#e0c9a3 40%,#b63a2c 70%,#8e6a48 100%)}
.moment-three{left:704px;background:radial-gradient(circle at 50% 40%,#e9e3da 0%,#9eaab8 45%,#2b3f6b 75%,#c8a888 100%)}
.notice{position:absolute;left:33px;top:968px;width:345px;font-family:"Lora",serif;font-size:22px;line-height:28px}
.notice p+p{margin-top:28px}
.contact{position:absolute;right:33px;top:952px;text-align:right}
.contact-title{font-family:"Lora",serif;font-weight:700;font-size:23px;line-height:26px;color:var(--green);text-transform:uppercase}
.contact-list{list-style:none;margin-top:6px;font-size:24px;line-height:34px}
.contact-list svg{width:18px;height:18px;margin-right:6px;vertical-align:-2px}
.tour{position:absolute;left:568px;top:1114px;width:388px;height:56px;border-radius:18px;background:var(--green);
  color:var(--blue-deep);font-family:"Lato",sans-serif;font-size:36px;line-height:56px;text-align:center;box-shadow:0 3px 0 var(--green-dark)}
</style>
</head>
<body>
<main class="flyer">
  <svg class="backdrop" viewBox="0 0 991 1200" aria-hidden="true">
    <defs>
      <linearGradient id="sea" x1="0" y1="0" x2="0" y2="1">
        <stop offset="0" stop-color="#2aa6df"/>
        <stop offset="1" stop-color="#1185c6"/>
      </linearGradient>
      <radialGradient id="table" cx="45%" cy="55%" r="60%">
        <stop offset="0" stop-color="#d9a66b"/>
        <stop offset=".5" stop-color="#b98148"/>
        <stop offset="1" stop-color="#7e5a3b"/>
      </radialGradient>
    </defs>
    <rect width="991" height="1200" fill="url(#sea)"/>
    <path d="M0 720 C300 660 600 780 991 710 V1200 H0 Z" fill="#3fb2e6" opacity=".35"/>
    <path d="M0 0 H991 V470 C820 500 560 330 0 362 Z" fill="#ffffff"/>
    <path d="M0 345 C250 320 500 360 700 450" fill="none" stroke="#b5d334" stroke-width="9"/>
    <path d="M0 366 C260 342 500 382 690 470" fill="none" stroke="#49b6e6" stroke-width="5" opacity=".7"/>
    <circle cx="805" cy="190" r="305" fill="#b5d334"/>
    <circle cx="805" cy="190" r="293" fill="#ffffff"/>
    <circle cx="815" cy="182" r="285" fill="#1d9bd7"/>
    <circle cx="815" cy="176" r="275" fill="url(#table)" role="img" aria-label="Photo: young children smiling at a classroom table with plates"/>
    <polygon points="500,818 482,804 482,832" fill="#0d5e93"/>
    <polygon points="821,818 803,804 803,832" fill="#0d5e93"/>
    <rect x="0" y="1180" width="991" height="20" fill="#b5d334"/>
  </svg>

  <div class="brand">TB Academy</div>
  <p class="headline">Montessori graduates are<br>leading the top companies<br>of our time</p>

  <div class="photo photo-stage" role="img" aria-label="Photo: children in white and red performing on a stage"></div>
  <span class="pin"></span>

  <h2 class="enroll-title">Enrollment is open now for<br>all four programs:</h2>
  <ul class="programs">
    <li><b>Toddler:</b> 18months (or as soon as the child is able to walk) - 3 years</li>
    <li><b>Casa:</b> Preschool to Senior Kindergarten (3 years to 6 years)</li>
    <li><b>Elementary:</b> Grades 1 to 6</li>
    <li><b>Junior High:</b> Grades 7 to 8z</li>
  </ul>

  <svg class="badge" viewBox="-140 -140 280 280" aria-hidden="true">
    <g fill="#b5d334">
      <rect x="-99" y="-99" width="198" height="198"/>
      <rect x="-99" y="-99" width="198" height="198" transform="rotate(15)"/>
      <rect x="-99" y="-99" width="198" height="198" transform="rotate(30)"/>
      <rect x="-99" y="-99" width="198" height="198" transform="rotate(45)"/>
      <rect x="-99" y="-99" width="198" height="198" transform="rotate(60)"/>
      <rect x="-99" y="-99" width="198" height="198" transform="rotate(75)"/>
    </g>
  </svg>
  <p class="badge-text"><span class="lead">We are an</span><span class="strong">ACCREDITED</span><span class="strong">MONTESSORI</span><span class="strong">SCHOOL</span></p>

  <h2 class="languages"><span class="accent">LANGUAGES</span> PUNJABI, HINDI AND ITALIA</h2>
  <p class="faith">WE OFFER THEIR FAITH AND CULTURAL EDUCATION AS WELL</p>

  <div class="photo moment moment-one" role="img" aria-label="Photo: a toddler working with Montessori counting materials on the floor"></div>
  <div class="photo moment moment-two" role="img" aria-label="Photo: a boy in a turban and red sweater writing at a desk"></div>
  <div class="photo moment moment-three" role="img" aria-label="Photo: a teacher guiding a student with his writing"></div>

  <div class="notice">
    <p>Fees for children under age of 6 can be claimed in Taxes as day care expense.</p>
    <p>So, there is no reason to miss providing our children the best that we can in education.</p>
  </div>

  <section class="contact">
    <h3 class="contact-title">Our contact<br>intformation:</h3>
    <ul class="contact-list">
      <li><svg viewBox="0 0 20 20"><rect x="1" y="4" width="18" height="12" fill="#0d5e93"/><path d="M1 4 L10 11 L19 4" fill="none" stroke="#fff" stroke-width="1.5"/></svg>info@tbacademy.net</li>
      <li><svg viewBox="0 0 20 20"><path d="M5 2 L8 2 L9 6 L7 8 C8 11 9 12 12 13 L14 11 L18 12 L18 15 C18 17 16 18 14 18 C8 17 3 12 2 6 C2 4 3 2 5 2 Z" fill="#0d5e93"/></svg>416 527 3962</li>
      <li><svg viewBox="0 0 20 20"><circle cx="10" cy="10" r="8" fill="#0d5e93"/><path d="M2 10 H18 M10 2 C6 6 6 14 10 18 M10 2 C14 6 14 14 10 18" fill="none" stroke="#fff" stroke-width="1.2"/></svg>www.tbacademy.net</li>
    </ul>
  </section>

  <div class="tour">BOOK A TOUR!</div>
</main>
</body>
</html>
```